ebook cover for book three in a spiritual iconic series: bold, simple, easy to manage!

The Drift is the third in a series of memoirs about one woman's spiritual journey over ten years. A PhD, the woman wants to appeal to a broad market and an intellectual market as well as the women's market that makes the core audience. Every Last Plum is the second book and its cover is currently also commissioned here on Pixel Harbour if you want to search it. We Ate Pears was the first and its cover is attached for your reference. Please keep the same: the white background, the shade of red for the title, the font for the subtitle and colour, but change the title font and how you use the colour scheme. We look for a slightly enigmatic and also strikingly simple image. The tin can in We Ate Pears is where to start. For Every Last Plum we have asked for a single Lexitile tablet, the X. Here, we are thinking of the winking smiley attached, but the image needs some photoshopping to make the face a bit more to yellow cold, remove the red ring and so on. The colours to pick from are greys, purple, red, orange, yellow, as with the colors in the flash of light on the tin can in Ate Pears. The idea there was to capture an explosion to new ideas while referencing a key scene involving cooking with tomatoes!

The Drift

Book details:
Title: The Drift
Subtitle: Brother Aldous introduces Veridonne
Image ideas: Winking smiley attached, princess castle in the right colours, magic wand.
Author: Marta Quillon, Ph.D
Strap quote: "Marta Quillon is phenomenal in the true sense of the word. Phenomenons occur around her," Rosa Finch, Teacher and spiritual healer

```html
<!DOCTYPE html>
<html lang="en">
<head>
<meta charset="utf-8">
<title>The Drift – Marta Quillon Ph.D.</title>
<link rel="stylesheet" href="https://fonts.googleapis.com/css2?family=Oswald:wght@700&family=Open+Sans:wght@400;600&display=swap">
<style>
  :root {
    --paper: #ffffff;
    --title-red: #c4161c;
    --ink-grey: #4a4a4a;
    --author-grey: #777777;
    --quote-ink: #2e2e2e;
    --sun-light: #fff06a;
    --sun-mid: #fbd30e;
    --sun-deep: #e7a800;
  }
  * { margin: 0; padding: 0; box-sizing: border-box; }
  html, body {
    width: 800px;
    height: 1200px;
    overflow: hidden;
    background: var(--paper);
  }
  .cover {
    position: relative;
    width: 800px;
    height: 1200px;
    background: var(--paper);
    font-family: "Open Sans", Arial, sans-serif;
  }
  .endorsement {
    position: absolute;
    top: 30px;
    left: 40px;
    right: 40px;
    font-size: 17px;
    line-height: 1.55;
    font-weight: 600;
    text-transform: uppercase;
    color: var(--quote-ink);
  }
  .title {
    position: absolute;
    top: 160px;
    left: 0;
    width: 100%;
    text-align: center;
    font-family: "Oswald", "Arial Narrow", sans-serif;
    font-size: 96px;
    font-weight: 700;
    line-height: 1;
    letter-spacing: 1px;
    text-transform: uppercase;
    color: var(--title-red);
  }
  .subtitle {
    position: absolute;
    top: 318px;
    left: 0;
    width: 100%;
    text-align: center;
    font-size: 36px;
    font-weight: 600;
    line-height: 1.4;
    letter-spacing: 2px;
    text-transform: uppercase;
    color: var(--ink-grey);
  }
  .emblem {
    position: absolute;
    top: 450px;
    left: 120px;
    width: 560px;
    height: 560px;
  }
  .author {
    position: absolute;
    top: 1062px;
    left: 0;
    width: 100%;
    text-align: center;
    font-size: 44px;
    font-weight: 400;
    letter-spacing: 5px;
    text-transform: uppercase;
    color: var(--author-grey);
  }
</style>
</head>
<body>
  <main class="cover">
    <p class="endorsement">
      “Marta Quillon is phenomenal in the true sense of the word. Phenomenons occur around her” – Rosa Finch, teacher and spiritual healer
    </p>

    <h1 class="title">The Drift</h1>

    <h2 class="subtitle">Brother Aldous<br>introduces Veridonne</h2>

    <svg class="emblem" viewBox="0 0 560 560" role="img" aria-label="Yellow winking smiley with a glint of light at its upper left">
      <defs>
        <radialGradient id="sun-glow" cx="35%" cy="25%" r="80%">
          <stop offset="0%" stop-color="var(--sun-light)"/>
          <stop offset="60%" stop-color="var(--sun-mid)"/>
          <stop offset="100%" stop-color="var(--sun-deep)"/>
        </radialGradient>
      </defs>
      <circle cx="280" cy="280" r="278" fill="url(#sun-glow)"/>
    </svg>

    <p class="author">Marta Quillon Ph.D.</p>
  </main>
</body>
</html>
```